Virtual Reality medical education company

We are a new company that is offering virtual reality medical simulation suites. I have had a go at the initial web design www.brellowanstudio-example.com but as you can see I am no web designer!
I have the logo and some text which I'd like you to use - also some images. Any help with the SEO would be appreciated.

Target Market(s)

Students and faculty in medical and applied medical degrees

Industry/Entity Type

Education

Coding

Coded - Design and coding required

Number of Pages Required

5+ page

Font styles to use
Sans Serif

Requirements
Must have
• Home, Benefits, Simulation, Why Virtual, Modules, Contact Us
• Virtual reality scenes, either people using it or what they see.
• This is the patient we are using http://www.plexomarket-example.com/3d-models/rigged-hospital-patient-3d-max/4830291
Nice to have
• QRN Lumo or Pentara Drift headsets being worn
Should not have
• Non VR simulation, real patients/models, students looking at computer screens

```html
<!DOCTYPE html>
<html lang="en">
<head>
<meta charset="utf-8">
<title>Brellowan Sim Studio</title>
<link rel="stylesheet" href="https://fonts.googleapis.com/css2?family=Cinzel:wght@400;700&family=Lato:wght@400;700&display=swap">
<style>
:root{
  --ink:#1b1b1b;
  --navy:#2c3491;
  --blue:#1c8ad3;
  --brand:#2460b8;
  --grey-band:#ededed;
  --btn:#222;
  --footer:#141414;
  --footer-bar:#0b0b0b;
  --muted:#555;
  --white:#fff;
}
*{margin:0;padding:0;box-sizing:border-box}
html,body{width:1200px;height:2586px;overflow:hidden;background:var(--white)}
body{position:relative;font-family:'Lato',sans-serif;color:var(--ink)}
.abs{position:absolute}
.serif{font-family:'Cinzel',serif}

.top-rule{left:0;top:0;width:1200px;height:4px;background:#333}
.header{left:0;top:4px;width:1200px;height:110px;background:linear-gradient(#fff,#eee)}
.brand-name{left:164px;top:44px;display:flex;align-items:center;gap:10px;font-family:'Cinzel',serif;font-size:24px;font-weight:700;color:var(--brand)}
.brand-dot{width:18px;height:18px;border-radius:50%;background:var(--brand)}
.pill{top:46px;height:28px;border-radius:14px;background:#e3e3e3;border:1px solid #cfcfcf;display:flex;align-items:center;font-size:13px;color:#333;padding-right:12px}
.pill-icon{width:22px;height:22px;border-radius:50%;background:var(--navy);margin:0 8px 0 3px;display:flex;align-items:center;justify-content:center}
.pill.phone{left:583px;width:136px}
.pill.mail{left:731px;width:307px;font-size:12px}

.nav{left:0;top:114px;width:1200px;height:41px;background:var(--navy)}
.nav a{position:absolute;top:0;height:41px;line-height:41px;font-family:'Cinzel',serif;font-size:17px;color:#fff;text-decoration:none;letter-spacing:.5px}
.nav a.active{background:var(--blue);padding:0 18px}
.nav .sep{position:absolute;top:10px;width:1px;height:22px;background:rgba(255,255,255,.35)}

.hero{left:0;top:155px;width:1200px;height:523px;background:linear-gradient(160deg,#7d7a6c 0%,#a9a59a 40%,#8f8c82 70%,#565349 100%)}
.hero-caption{left:664px;top:252px;width:334px;height:334px;border-radius:50%;background:rgba(20,20,20,.82);display:flex;align-items:center;justify-content:center;text-align:center;padding:40px;font-family:'Cinzel',serif;font-size:23px;line-height:32px;color:#fff}
.hero-arrow{top:362px;width:56px;height:56px;border-radius:50%;background:rgba(30,30,30,.7);display:flex;align-items:center;justify-content:center}

.section-title{left:0;width:1200px;text-align:center;font-family:'Cinzel',serif;font-size:28px;color:var(--ink)}
.title-rule{height:2px;background:linear-gradient(90deg,transparent,#999 15%,#999 85%,transparent)}
.brand-inline{color:var(--brand)}
.body-copy{font-size:13px;line-height:21px;color:#333;text-align:center}
.btn{height:33px;border-radius:4px;background:var(--btn);color:#fff;font-size:13px;display:flex;align-items:center;justify-content:center;letter-spacing:.3px}

.services{left:0;top:984px;width:1200px;height:509px;background:var(--grey-band)}
.service-ring{top:1107px;width:190px;height:190px;border-radius:50%;border:7px solid var(--navy);background:#fff;padding:8px}
.service-ring div{width:100%;height:100%;border-radius:50%}
.service-name{width:340px;text-align:center;font-family:'Cinzel',serif;font-size:20px;font-weight:700;top:1322px}
.service-text{width:260px;text-align:center;font-size:12.5px;line-height:21px;color:#333;top:1359px}

.benefit{top:1493px;width:600px;height:395px}
.benefit.students{left:0;background:linear-gradient(120deg,#3a9be0,#1e87d0 60%,#3a9fe4)}
.benefit.institutes{left:600px;background:linear-gradient(120deg,#2c2c2c,#1f1f1f 55%,#3a2222)}
.benefit-icon{top:72px;width:104px;height:104px;border-radius:50%;border:3px solid #fff;left:248px;display:flex;align-items:center;justify-content:center}
.benefit-head{top:200px;left:0;width:600px;text-align:center;font-family:'Cinzel',serif;font-size:28px;line-height:33px;color:#fff}
.benefit-text{top:281px;left:130px;width:340px;text-align:center;font-size:12.5px;line-height:20px;color:#fff}

.testimonial-photo{top:2010px;width:94px;height:94px;border-radius:50%;border:4px solid var(--blue);background:linear-gradient(#e9d6c4,#c8a88c)}
.quote-mark{top:2005px;font-family:Georgia,serif;font-size:44px;color:#ccc;line-height:1}
.testimonial-text{top:2014px;width:302px;font-size:12px;line-height:21px;color:#333}
.testimonial-rule{top:2124px;height:1px;background:linear-gradient(90deg,transparent,#bbb 20%,#bbb)}
.testimonial-name{top:2138px;width:240px;text-align:center;font-size:11.5px;font-weight:700;color:var(--blue)}

.footer{left:0;top:2224px;width:1200px;height:319px;background:var(--footer)}
.footer-bar{left:0;top:2543px;width:1200px;height:43px;background:var(--footer-bar);color:#bbb;font-size:11.5px;text-align:center;line-height:43px}
.footer-head{top:2310px;font-family:'Cinzel',serif;font-size:14px;color:#fff;letter-spacing:.5px}
.footer-head::after{content:"";display:block;margin-top:8px;height:1px;background:#3a3a3a;width:120%}
.quick-links{top:2344px;left:164px;list-style:none;font-size:11px;line-height:22.5px;color:#ddd}
.quick-links li::before{content:"• ";color:#ddd}
.quick-links li.current{color:var(--blue)}
.contact-row{left:303px;display:flex;gap:10px;font-size:11px;line-height:17px;color:#ddd}
.field{left:598px;width:188px;background:#333;border:1px solid #3d3d3d;color:#ddd;font-size:11px;padding:8px}
.submit{left:598px;top:2488px;width:83px;height:32px;background:var(--blue);color:#fff;font-size:14px;font-weight:700;display:flex;align-items:center;justify-content:center}
.footer-brand{left:820px;top:2350px;width:230px;text-align:center;font-family:'Cinzel',serif;font-size:22px;line-height:28px;color:#ddd}
.footer-brand-mark{margin:0 auto 16px;width:60px;height:60px;border-radius:50%;background:#555}
</style>
</head>
<body>

<div class="abs top-rule"></div>
<header class="abs header"></header>
<div class="abs brand-name"><span class="brand-dot"></span>Brellowan Sim Studio</div>
<div class="abs pill phone"><span class="pill-icon"><svg width="12" height="12" viewBox="0 0 24 24"><path fill="#fff" d="M6.6 10.8a15 15 0 0 0 6.6 6.6l2.2-2.2c.3-.3.7-.4 1-.2 1.1.4 2.3.6 3.6.6.6 0 1 .4 1 1V20c0 .6-.4 1-1 1A17 17 0 0 1 3 4c0-.6.4-1 1-1h3.5c.6 0 1 .4 1 1 0 1.3.2 2.5.6 3.6.1.3 0 .7-.2 1z"/></svg></span>123 456 7890</div>
<div class="abs pill mail"><span class="pill-icon"><svg width="12" height="10" viewBox="0 0 24 18"><rect x="1" y="1" width="22" height="16" rx="2" fill="#fff"/><path d="M2 2l10 8 10-8" fill="none" stroke="#2c3491" stroke-width="2"/></svg></span>Tomas.Reval@brellowanstudio-example.com</div>

<nav class="abs nav">
  <a class="active" style="left:162px">HOME</a>
  <a style="left:288px">BENEFITS</a><span class="sep" style="left:400px"></span>
  <a style="left:428px">SIMULATION</a><span class="sep" style="left:568px"></span>
  <a style="left:596px">WHY VIRTUAL</a><span class="sep" style="left:745px"></span>
  <a style="left:772px">MODULES</a><span class="sep" style="left:883px"></span>
  <a style="left:910px">CONTACT US</a>
</nav>

<section class="abs hero" role="img" aria-label="Virtual reality scene of a patient lying on an X-ray table under imaging equipment in a tiled clinical room"></section>
<div class="abs hero-caption">Our technology allows the students or tutor to “feel” lumps, such as bony landmarks, on a patient.</div>
<div class="abs hero-arrow" style="left:22px"><svg width="16" height="24" viewBox="0 0 16 24"><path d="M13 2L3 12l10 10" fill="none" stroke="#ccc" stroke-width="2"/></svg></div>
<div class="abs hero-arrow" style="left:1120px"><svg width="16" height="24" viewBox="0 0 16 24"><path d="M3 2l10 10L3 22" fill="none" stroke="#ccc" stroke-width="2"/></svg></div>

<h1 class="abs section-title" style="top:725px;font-size:29px">Welcome to <span class="brand-inline">Brellowan Sim Studio</span></h1>
<div class="abs title-rule" style="left:362px;top:782px;width:476px"></div>
<p class="abs body-copy" style="left:180px;top:802px;width:840px">Lorem ipsum dolor sit amet, consectetuer adipiscing elit, sed diam nonummy nibh euismod tincidunt ut laoreet dolore magna aliquam erat volutpat. Ut wisi enim ad minim veniam, quis nostrud exerci tation ullamcorper suscipit lobortis nisl ut aliquip ex ea commodo consequat. Duis autem vel eum iriure dolor in hendrerit in vulputate velit esse molestie consequat, vel illum dolore eu feugiat nulla facilisis at vero eros et accumsan et iusto odio dignissim qui blandit praesent luptatum zzril delenit augue duis dolore te feugait nulla facilisi.</p>
<div class="abs btn" style="left:550px;top:915px;width:100px">READ MORE</div>

<section class="abs services"></section>
<h2 class="abs section-title" style="top:1022px">Our Services</h2>
<div class="abs title-rule" style="left:425px;top:1076px;width:350px"></div>

<div class="abs service-ring" style="left:181px"><div role="img" aria-label="Patient model standing in a hospital gown" style="background:linear-gradient(#f4f4f4,#dcdcdc)"></div></div>
<div class="abs service-ring" style="left:505px"><div role="img" aria-label="X-ray image of a pelvis" style="background:radial-gradient(#b5b5b5,#4a4a4a)"></div></div>
<div class="abs service-ring" style="left:829px"><div role="img" aria-label="Patient on an imaging table under equipment" style="background:linear-gradient(#cfd8e4,#8aa6c0)"></div></div>

<h3 class="abs service-name" style="left:106px">The Patient</h3>
<h3 class="abs service-name" style="left:430px">Exposure Setting and Imaging</h3>
<h3 class="abs service-name" style="left:754px">Equipment</h3>
<p class="abs service-text" style="left:146px">Brellowan Sim Studio has created different patients to reflect the...</p>
<p class="abs service-text" style="left:470px">Just like the clinical environment, imaging is conducted from behind...</p>
<p class="abs service-text" style="left:794px">Brellowan Sim Studio offers the latest computed radiography (CR)...</p>
<div class="abs btn" style="left:226px;top:1421px;width:100px">READ MORE</div>
<div class="abs btn" style="left:550px;top:1421px;width:100px">READ MORE</div>
<div class="abs btn" style="left:874px;top:1421px;width:100px">READ MORE</div>

<section class="abs benefit students" role="img" aria-label="Two students in scrubs working together, tinted blue">
  <div class="abs benefit-icon"><svg width="50" height="50" viewBox="0 0 24 24"><path fill="#fff" d="M2 10h4v11H2zM8 21h9c.8 0 1.5-.5 1.8-1.2l2.9-6.8c.2-.4.3-.8.3-1.2V10c0-1.1-.9-2-2-2h-6.3l1-4.6v-.3c0-.4-.2-.8-.4-1.1L13.2 1 8 6.6V21z"/></svg></div>
  <h2 class="abs benefit-head">Benefits for<br>Students</h2>
  <p class="abs benefit-text">Students require hands on learning which encourages them to actively think about information, make choices, and execute learning skills for defined physical tasks.</p>
</section>
<section class="abs benefit institutes" role="img" aria-label="Red heart model with a stethoscope on a dark background">
  <div class="abs benefit-icon"><svg width="54" height="54" viewBox="0 0 24 24" fill="none" stroke="#fff" stroke-width="1.4"><rect x="8" y="3" width="13" height="10"/><circle cx="5" cy="6" r="2" fill="#fff"/><path d="M5 9v7M3 12h8" /><path d="M12 10l3-3 2 2 3-3"/><circle cx="8" cy="19" r="1.3" fill="#fff"/><circle cx="12" cy="19" r="1.3" fill="#fff"/><circle cx="16" cy="19" r="1.3" fill="#fff"/><path d="M5 22h16"/></svg></div>
  <h2 class="abs benefit-head">Benefits for Training<br>Institutes</h2>
  <p class="abs benefit-text">For training institutes, having live radiation equipment means building special rooms for them to be housed in, with strengthened ceilings and radiation protected walls and floors.</p>
</section>

<h2 class="abs section-title" style="top:1920px">Clients Testimonials</h2>
<div class="abs title-rule" style="left:425px;top:1966px;width:380px"></div>

<div class="abs testimonial-photo" role="img" aria-label="Portrait of a client" style="left:165px"></div>
<span class="abs quote-mark" style="left:279px">“</span>
<p class="abs testimonial-text" style="left:281px;text-indent:30px">Lorem ipsum dolor sit amet, consect uer erwere adipiscing elit, sed diam nonummy nibh euis mod tincidunt ut laoreetml dolore magna aliquam erat volutpat. Utewi wisi enim ad minim veniam, quis nostrud exer.</p>
<div class="abs testimonial-rule" style="left:160px;width:420px"></div>
<div class="abs testimonial-name" style="left:265px">- Miss Arla Venmore</div>

<div class="abs testimonial-photo" role="img" aria-label="Portrait of a client" style="left:618px"></div>
<span class="abs quote-mark" style="left:735px">“</span>
<p class="abs testimonial-text" style="left:735px;text-indent:30px">Lorem ipsum dolor sit amet, consect uer erwere adipiscing elit, sed diam nonummy nibh euis mod tincidunt ut laoreetml dolore magna aliquam erat volutpat. Utewi wisi enim ad minim veniam, quis nostrud exer.</p>
<div class="abs testimonial-rule" style="left:615px;width:420px"></div>
<div class="abs testimonial-name" style="left:718px">- Miss Arla Venmore</div>

<svg class="abs" style="left:992px;top:2168px" width="36" height="12" viewBox="0 0 36 12"><circle cx="6" cy="6" r="4.5" fill="none" stroke="#1c8ad3"/><circle cx="6" cy="6" r="2.5" fill="#1c8ad3"/><circle cx="18" cy="6" r="3" fill="#ccc"/><circle cx="29" cy="6" r="3" fill="#ccc"/></svg>

<svg class="abs" style="left:0;top:2170px" width="1200" height="110" viewBox="0 0 1200 110">
  <path d="M0 20 C300 90 600 80 800 50 C950 28 1080 20 1200 40 L1200 110 L0 110Z" fill="#1c8ad3"/>
  <path d="M0 45 C300 110 620 100 820 72 C970 52 1090 48 1200 62 L1200 110 L0 110Z" fill="#141414"/>
</svg>

<footer class="abs footer"></footer>
<h4 class="abs footer-head" style="left:164px">Quick Links</h4>
<ul class="abs quick-links">
  <li class="current">Home</li><li>Benefits</li><li>Simulation</li><li>Why Virtual</li><li>Modules</li><li>Contact Us</li>
</ul>

<h4 class="abs footer-head" style="left:303px">Contact Details</h4>
<div class="abs contact-row" style="top:2350px"><svg width="12" height="16" viewBox="0 0 12 16"><path d="M6 0a6 6 0 0 1 6 6c0 4-6 10-6 10S0 10 0 6a6 6 0 0 1 6-6z" fill="#1c8ad3"/><circle cx="6" cy="6" r="2" fill="#141414"/></svg><span>Brellowan Sim Studio<br>123, Lorem ipsum dolor sit amet, nsectet uer<br>tiere adipiscing elit, sed diam nonummy</span></div>
<div class="abs contact-row" style="top:2412px"><svg width="12" height="12" viewBox="0 0 24 24"><path fill="#1c8ad3" d="M6.6 10.8a15 15 0 0 0 6.6 6.6l2.2-2.2c.3-.3.7-.4 1-.2 1.1.4 2.3.6 3.6.6.6 0 1 .4 1 1V20c0 .6-.4 1-1 1A17 17 0 0 1 3 4c0-.6.4-1 1-1h3.5c.6 0 1 .4 1 1 0 1.3.2 2.5.6 3.6.1.3 0 .7-.2 1z"/></svg><span>123 456 7890</span></div>
<div class="abs contact-row" style="top:2446px"><svg width="12" height="10" viewBox="0 0 24 18"><rect x="1" y="1" width="22" height="16" rx="2" fill="#1c8ad3"/><path d="M2 2l10 8 10-8" fill="none" stroke="#141414" stroke-width="2"/></svg><span>Tomas.Reval@brellowanstudio-example.com</span></div>

<h4 class="abs footer-head" style="left:598px">Quick Contact</h4>
<div class="abs field" style="top:2350px;height:31px">Name</div>
<div class="abs field" style="top:2388px;height:29px">Email</div>
<div class="abs field" style="top:2424px;height:53px">Message</div>
<div class="abs submit">Submit</div>

<div class="abs footer-brand"><div class="footer-brand-mark"></div>Brellowan<br>Sim Studio</div>

<div class="abs footer-bar">Copyright © 2016 Brellowan Sim Studio. All Rights Reserved.</div>

</body>
</html>
```